Buch-/eBook-Cover für professionelles Finanzbuch
Die Zusammenarbeit hat mega Spaß gemacht. Die Wünsche wurden kompetent und prompt umgesetzt - absolut empfehlenswert!
Zielgruppe
Selbstständig in der Finanzaufklärung als Speaker und Verkäufer von Sachwerten
Aufgabenstellung
soll ein professionelles Finanzbuch sein von der Optik mit Foto von Technologiemetallen /Seltenen Erden

```html
<!DOCTYPE html>
<html lang="de">
<head>
<meta charset="utf-8">
<title>Technologiemetalle und Seltene Erden – Buchcover</title>
<link rel="stylesheet" href="https://fonts.googleapis.com/css2?family=Oswald:wght@500;700&family=Montserrat:wght@400;800&display=swap">
<style>
  :root {
    --stage: #dcdcdc;
    --cover-dark: #1c1d21;
    --gold: #c9a46a;
    --white: #ffffff;
    --paper: #f2f2f2;
    --silver-light: #f4f4f2;
    --silver-mid: #bdbcb8;
  }
  html, body {
    margin: 0;
    width: 1195px;
    height: 1200px;
    overflow: hidden;
    background: var(--stage);
  }
  .book-cover {
    position: absolute;
    left: 281px;
    top: 94px;
    width: 632px;
    height: 1012px;
    box-shadow: 0 18px 40px rgba(0,0,0,0.28);
  }
  .book-cover svg { display: block; }
  .author-name { font-family: "Oswald", sans-serif; font-weight: 500; fill: var(--white); }
  .kicker { font-family: "Oswald", sans-serif; font-weight: 500; fill: var(--gold); }
  .title-word { font-family: "Oswald", sans-serif; font-weight: 700; fill: url(#silver); }
  .connector { font-family: "Montserrat", sans-serif; font-weight: 800; fill: var(--white); }
  .subtitle { font-family: "Montserrat", sans-serif; font-weight: 400; fill: var(--white); }
</style>
</head>
<body>
<div class="book-cover">
  <svg width="632" height="1012" viewBox="0 0 632 1012" xmlns="http://www.w3.org/2000/svg">
    <defs>
      <linearGradient id="silver" x1="0" y1="0" x2="1" y2="0.3">
        <stop offset="0" stop-color="var(--silver-mid)"/>
        <stop offset="0.35" stop-color="var(--silver-light)"/>
        <stop offset="0.6" stop-color="#d6d5d1"/>
        <stop offset="0.8" stop-color="var(--silver-light)"/>
        <stop offset="1" stop-color="var(--silver-mid)"/>
      </linearGradient>
      <linearGradient id="chart-photo" x1="0" y1="0" x2="1" y2="1">
        <stop offset="0" stop-color="#111216"/>
        <stop offset="0.45" stop-color="#4a3c26"/>
        <stop offset="0.7" stop-color="#8a7045"/>
        <stop offset="0.85" stop-color="#7c8ea3"/>
        <stop offset="1" stop-color="#1c1d21"/>
      </linearGradient>
      <linearGradient id="photo-fade" x1="0" y1="0" x2="0" y2="1">
        <stop offset="0.6" stop-color="#1c1d21" stop-opacity="0"/>
        <stop offset="1" stop-color="#1c1d21" stop-opacity="1"/>
      </linearGradient>
      <radialGradient id="minerals" cx="0.5" cy="0.5" r="0.5">
        <stop offset="0" stop-color="#9a6a48"/>
        <stop offset="0.6" stop-color="#b58a5a"/>
        <stop offset="1" stop-color="#f2f2f2" stop-opacity="0"/>
      </radialGradient>
    </defs>

    <rect class="cover-base" width="632" height="1012" fill="var(--cover-dark)"/>

    <g role="img" aria-label="Foto: goldene und silberne Metallbarren als Balkendiagramm angeordnet">
      <rect width="632" height="345" fill="url(#chart-photo)"/>
      <rect width="632" height="345" fill="url(#photo-fade)"/>
    </g>

    <text class="author-name" x="316" y="60" text-anchor="middle" font-size="24" textLength="200" lengthAdjust="spacingAndGlyphs">LUKAS VENHORST</text>

    <text class="kicker" x="316" y="287" text-anchor="middle" font-size="21" textLength="338" lengthAdjust="spacing">JAHRHUNDERTCHANCE</text>

    <text class="title-word" x="315" y="388" text-anchor="middle" font-size="100" textLength="474" lengthAdjust="spacingAndGlyphs">TECHNOLOGIE-</text>
    <text class="title-word" x="316" y="480" text-anchor="middle" font-size="100" textLength="289" lengthAdjust="spacingAndGlyphs">METALLE</text>
    <text class="connector" x="316" y="513" text-anchor="middle" font-size="21" textLength="49" lengthAdjust="spacingAndGlyphs">UND</text>
    <text class="title-word" x="316" y="640" text-anchor="middle" font-size="140" textLength="388" lengthAdjust="spacingAndGlyphs">SELTENE</text>
    <text class="title-word" x="316" y="762" text-anchor="middle" font-size="140" textLength="296" lengthAdjust="spacingAndGlyphs">ERDEN</text>

    <text class="subtitle" x="316" y="792" text-anchor="middle" font-size="21" textLength="438" lengthAdjust="spacingAndGlyphs">VOM SELTENEN ZUM UNVERZICHTBAREN</text>

    <path class="torn-edge" fill="var(--paper)" stroke="#cfcfcf" stroke-width="1.5"
      d="M0 830 L22 827 L40 831 L58 826 L80 830 L104 825 L120 829 L140 822 L158 828 L176 826 L196 815 L214 820 L232 812 L250 818 L268 810 L290 816 L310 811 L330 819 L352 813 L372 820 L394 815 L414 823 L436 817 L458 826 L480 820 L500 827 L522 823 L544 829 L566 824 L590 830 L610 826 L632 829 L632 1012 L0 1012 Z"/>

    <g role="img" aria-label="Foto: kleiner Haufen bunter Erze und Metallpulver">
      <ellipse cx="321" cy="915" rx="140" ry="55" fill="url(#minerals)"/>
    </g>
  </svg>
</div>
</body>
</html>
```